Curbglide-Lounge Theme For Forums!

We are looking for a theme for our forums. The forums are ran off Invision Power Boards. We have a basic theme on there now but we want more our own feel. If possible have some longboarding accept incorporated in the theme. We want the theme to have some red in it to match our logo. Curbglide-lounge.com

Target Market(s)

Skatingboarding & Longboarding

Coding

Coded - Design and coding required

Number of Pages Required

1 page

Colors
f04a50

```html
<!DOCTYPE html>
<html lang="en">
<head>
<meta charset="utf-8">
<title>Curbglide-Lounge Forums</title>
<link href="https://fonts.googleapis.com/css2?family=Roboto:wght@400;500;700&family=Roboto+Condensed:wght@700&display=swap" rel="stylesheet">
<style>
:root{
  --red:#f04a50;
  --red-dark:#d63a40;
  --page:#efe4e5;
  --white:#ffffff;
  --ink:#333333;
  --muted:#888888;
  --dark:#3a3a3a;
  --darker:#2e2e2e;
  --line:#e2e2e2;
  --soft:#f2f2f2;
  --head:#e9e9e9;
}
*{box-sizing:border-box;margin:0;padding:0}
html,body{width:857px;height:1200px;overflow:hidden}
body{background:var(--page);font-family:"Roboto",Arial,sans-serif;color:var(--ink);font-size:11px}
a{color:inherit;text-decoration:none}

.site-header{background:var(--white);height:62px;display:flex;align-items:center;justify-content:space-between;padding:0 70px}
.brand{display:flex;align-items:center;gap:8px;color:var(--red);font-weight:700;font-size:19px;letter-spacing:.3px}
.brand-mark{width:16px;height:16px;background:var(--red)}
.user-box{display:flex;align-items:center;gap:8px}
.user-avatar{width:32px;height:32px;border-radius:50%;background:linear-gradient(135deg,#c9b8a8,#8c7b6c)}
.user-name{font-weight:700;font-size:11px}
.user-links{font-size:8px;color:var(--muted);margin-top:2px}
.user-caret{width:0;height:0;border-left:4px solid transparent;border-right:4px solid transparent;border-top:5px solid var(--muted)}

.main-nav{background:var(--soft);height:38px;border-bottom:1px solid var(--line);display:flex;align-items:center;justify-content:space-between;padding:0 70px}
.nav-links{display:flex;gap:26px;font-weight:700;font-size:11px;letter-spacing:.4px}
.search{display:flex}
.search-field{width:150px;height:24px;background:var(--white);border:1px solid var(--line);font-size:10px;color:var(--muted);padding:6px 8px}
.search-button{width:26px;height:24px;background:var(--red);display:flex;align-items:center;justify-content:center}

.welcome{padding:0 70px}
.welcome-row{display:flex;justify-content:space-between;align-items:center}
.welcome-row.top{margin-top:20px}
.welcome-title{font-family:"Roboto Condensed",Arial,sans-serif;font-size:19px;font-weight:700;letter-spacing:.3px}
.quick-links{font-size:8px;font-weight:500;letter-spacing:.4px}
.welcome-row.bottom{margin-top:8px}
.auth-links{display:flex;gap:16px;font-size:8px;font-weight:500}
.auth-links span::before{content:"";display:inline-block;width:6px;height:6px;background:var(--red);border-radius:50%;margin-right:5px}
.actions{display:flex;gap:8px}
.btn{border:1.5px solid var(--red);color:var(--red);border-radius:14px;font-size:9px;font-weight:700;padding:7px 12px;letter-spacing:.3px}

.panel{background:var(--white);margin:20px 70px 0;}
.panel-title{background:var(--dark);color:var(--white);text-align:center;font-family:"Roboto Condensed",Arial,sans-serif;font-weight:700;font-size:15px;height:32px;line-height:32px;letter-spacing:.6px}
.forum-panel{padding:0 0 16px;border:12px solid var(--white);border-top:none}
.forum-panel .panel-title{margin:0 -12px}

.forum-table{width:100%;border-collapse:collapse}
.forum-table th{background:var(--head);font-size:9px;font-weight:700;height:26px;letter-spacing:.4px}
.forum-table td{border-bottom:1px solid var(--line);height:52px;font-size:9px}
.forum-table .count{text-align:center;width:60px;border-left:1px solid var(--line)}
.forum-table .last{width:170px;border-left:1px solid var(--line);padding-left:12px}
.forum-cell{display:flex;align-items:center;gap:12px;padding-left:12px}
.forum-name{color:var(--red);font-weight:700;font-size:9px}
.forum-desc{color:var(--muted);font-size:7px;margin-top:3px}
.last-date{display:flex;align-items:center;gap:4px;color:#555;font-size:7px}
.last-by{font-size:7px;color:#555;margin-top:3px}
.last-by b{color:var(--red)}

.board-links{text-align:right;margin:16px 70px 0;font-size:8px;font-weight:500;letter-spacing:.3px}

.stats-panel{margin-top:18px;padding-bottom:14px}
.stats-tabs{background:#555;color:var(--white);display:flex;justify-content:center;gap:10px;height:24px;align-items:center;font-size:8px;font-weight:700;letter-spacing:.3px}
.stat-block{margin:8px 12px 0}
.stat-head{background:var(--head);height:26px;display:flex;align-items:center;gap:8px;padding:0 10px;font-size:9px;font-weight:700}
.stat-icon{width:10px;height:10px;background:var(--red);border-radius:2px}
.stat-body{padding:9px 28px 12px;font-size:8px;color:#555;line-height:14px}
.stat-body b{color:var(--red)}

.site-footer{text-align:center;font-size:8px;color:#666;margin-top:22px}
</style>
</head>
<body>
<header class="site-header">
  <div class="brand"><span class="brand-mark"></span>Curbglide-Lounge</div>
  <div class="user-box">
    <div>
      <div class="user-name">JOHN DOE</div>
      <div class="user-links">DASHBOARD | HELP</div>
    </div>
    <div class="user-avatar" role="img" aria-label="Member profile photo"></div>
    <span class="user-caret"></span>
  </div>
</header>

<nav class="main-nav">
  <div class="nav-links"><a>FORUMS</a><a>HELP</a><a>MEMBERS</a><a>CALENDAR</a></div>
  <div class="search">
    <div class="search-field">Search</div>
    <div class="search-button"><svg width="11" height="11" viewBox="0 0 12 12"><circle cx="5" cy="5" r="3.6" fill="none" stroke="#fff" stroke-width="1.6"/><line x1="7.6" y1="7.6" x2="11" y2="11" stroke="#fff" stroke-width="1.6"/></svg></div>
  </div>
</nav>

<section class="welcome">
  <div class="welcome-row top">
    <h1 class="welcome-title">WELCOME JOHN!</h1>
    <div class="quick-links">GUIDELINES &nbsp;|&nbsp; VIEW NEW CONTENT</div>
  </div>
  <div class="welcome-row bottom">
    <div class="auth-links"><span>LOGIN</span><span>REGISTER</span></div>
    <div class="actions"><a class="btn">WATCH FORUM</a><a class="btn">START NEW TOPIC</a></div>
  </div>
</section>

<section class="panel forum-panel">
  <h2 class="panel-title">A TEST ROBOT</h2>
  <table class="forum-table">
    <thead><tr><th>FORUM</th><th>TOPICS</th><th>REPLIES</th><th>LAST POST INFO</th></tr></thead>
    <tbody>
      <tr>
        <td><div class="forum-cell"><svg width="16" height="14" viewBox="0 0 16 14"><path d="M1 1h14v9H6l-4 3v-3H1z" fill="#bbb"/></svg><div><div class="forum-name">A Test Forum</div><div class="forum-desc">A sample forum for testing the new layout</div></div></div></td>
        <td class="count">1</td><td class="count">1</td>
        <td class="last"><div class="last-date"><svg width="8" height="8" viewBox="0 0 8 8"><rect x=".5" y="1" width="7" height="6.5" fill="none" stroke="#999"/><line x1=".5" y1="3" x2="7.5" y2="3" stroke="#999"/></svg>Apr 7 2007, 07:32 PM</div><div class="last-by">Re: Welcome! &nbsp;| &nbsp;By: <b>Board Team</b></div></td>
      </tr>
      <tr>
        <td><div class="forum-cell"><svg width="16" height="14" viewBox="0 0 16 14"><path d="M1 1h14v9H6l-4 3v-3H1z" fill="#bbb"/></svg><div><div class="forum-name">A Test Forum</div><div class="forum-desc">A sample forum for testing the new layout</div></div></div></td>
        <td class="count">1</td><td class="count">1</td>
        <td class="last"><div class="last-date"><svg width="8" height="8" viewBox="0 0 8 8"><rect x=".5" y="1" width="7" height="6.5" fill="none" stroke="#999"/><line x1=".5" y1="3" x2="7.5" y2="3" stroke="#999"/></svg>Apr 7 2007, 07:32 PM</div><div class="last-by">Re: Welcome! &nbsp;| &nbsp;By: <b>Board Team</b></div></td>
      </tr>
      <tr>
        <td><div class="forum-cell"><svg width="16" height="14" viewBox="0 0 16 14"><path d="M1 1h14v9H6l-4 3v-3H1z" fill="#bbb"/></svg><div><div class="forum-name">A Test Forum</div><div class="forum-desc">A sample forum for testing the new layout</div></div></div></td>
        <td class="count">1</td><td class="count">1</td>
        <td class="last"><div class="last-date"><svg width="8" height="8" viewBox="0 0 8 8"><rect x=".5" y="1" width="7" height="6.5" fill="none" stroke="#999"/><line x1=".5" y1="3" x2="7.5" y2="3" stroke="#999"/></svg>Apr 7 2007, 07:32 PM</div><div class="last-by">Re: Welcome! &nbsp;| &nbsp;By: <b>Board Team</b></div></td>
      </tr>
    </tbody>
  </table>
</section>

<div class="board-links">DELETE COOKIES SET BY THIS BOARD &nbsp;|&nbsp; MARK ALL POSTS AS READ</div>

<section class="panel stats-panel">
  <h2 class="panel-title">BOARD STATISTICS</h2>
  <div class="stats-tabs"><span>TODAY'S ACTIVE TOPICS</span>|<span>THE MODERATING TEAM</span>|<span>TODAY'S TOP 20 POSTERS</span>|<span>OVERALL TOP 20 POSTERS</span></div>

  <div class="stat-block">
    <div class="stat-head"><span class="stat-icon"></span>2 User(s) active in the past 15 minutes</div>
    <div class="stat-body">2 guests, 0 members, 0 anonymous members<br>Show detailed by: <b>LAST CLICK</b>, <b>MEMBER NAME</b></div>
  </div>
  <div class="stat-block">
    <div class="stat-head"><span class="stat-icon"></span>A Test Forum</div>
    <div class="stat-body">No Members are celebrating a birthday today</div>
  </div>
  <div class="stat-block">
    <div class="stat-head"><span class="stat-icon"></span>Forthcoming Calendar Events within the next 5 days</div>
    <div class="stat-body">There are no forthcoming calendar events</div>
  </div>
  <div class="stat-block">
    <div class="stat-head"><span class="stat-icon"></span>Board Statistics</div>
    <div class="stat-body">Our members have made a total of 1 posts<br>We have 1 registered members<br>The newest member is <b>admin</b><br>Most users ever online was 2 on <b>Today, 08:00 AM</b></div>
  </div>
</section>

<footer class="site-footer">© 2016, Curbglide-Lounge Forums All Rights Reserved</footer>
</body>
</html>
```